Residential improvers, A Cozy Perch 2 Go *

Cozy Perch 2 Go is a real estate company specializing in turning unloved properties into improved, happy places to live. We specialize in thoughtfully-improved residential properties for buyers or renters. Our company needs a business card that reflects the renovated homes we create using green and Feng Shui principles,

Please disregard the images we submitted. We are looking for an abstract, sophisticated elegant design. No eggs in a nest ... nothing cute. The image can be soft.
Updates

Aloha (hello) all designers. We are a serious property investment/improvement company. We strive to be unique, renovating with style and elegance. Our business card must portray the same message. We thought the nest and flower might be "it" ... clearly it's not, once we saw what you submitted. Please revisit the brief as it was modified yesterday. Mahalo for your input! We look forward to hearing from all designers that have been invited.

Industry/Entity Type

Real Estate Development

Contact Information for Business Card

We will have separate business cards for
1) Corabeth Lindqvist 808-555-0173 corabeth@mailbrook.test
2) Marla Fenwright 808-555-0198 marlafenwright@mailbrook.test
** can we add the website later ... in the process of approval.
Investors * Renovators * Connectors

Font styles to use
Sans Serif

Colors
cadf82

Requirements
Must have
• a feng shui feel ... modern. Color - green with black print.
Nice to have
• A Cozy Perch 2 Go

```html
<!DOCTYPE html>
<html lang="en">
<head>
<meta charset="utf-8">
<title>A Cozy Perch 2 Go — Business Card</title>
<link href="https://fonts.googleapis.com/css2?family=Open+Sans:wght@400;600&display=swap" rel="stylesheet">
<style>
  :root {
    --backdrop: #efece6;
    --card-white: #ffffff;
    --brand-green: #adc06b;
    --accent-green: #a3b85f;
    --ink: #111111;
    --on-green: #ffffff;
    --shadow: rgba(60, 45, 25, 0.22);
  }
  * { box-sizing: border-box; margin: 0; padding: 0; }
  html, body {
    width: 1200px; height: 942px; overflow: hidden;
    background: var(--backdrop);
    font-family: "Open Sans", Arial, sans-serif;
  }
  .canvas {
    position: relative; width: 1200px; height: 942px;
  }
  .card {
    position: absolute; top: 322px;
    width: 520px; height: 298px;
    box-shadow: 0 10px 24px var(--shadow);
  }
  .card--front { left: 50px; background: var(--card-white); }
  .card--back  { left: 630px; background: var(--brand-green); }

  /* Brand name lockup */
  .brand {
    position: absolute; display: flex; align-items: center; gap: 10px;
    font-weight: 400; white-space: nowrap;
  }
  .brand__mark { width: 12px; height: 12px; }
  .card--front .brand { left: 44px; top: 88px; font-size: 24px; color: var(--ink); }
  .card--front .brand__mark { background: var(--accent-green); }
  .card--back .brand {
    left: 0; right: 0; top: 104px; justify-content: center;
    font-size: 34px; color: var(--on-green);
  }
  .card--back .brand__mark { background: var(--on-green); width: 16px; height: 16px; }

  .divider {
    position: absolute; left: 282px; top: 150px;
    width: 1px; height: 110px; background: var(--accent-green);
  }

  .contact { position: absolute; left: 304px; top: 138px; }
  .contact__name {
    font-size: 22px; font-weight: 400; color: var(--ink);
    letter-spacing: -0.2px; margin-bottom: 12px;
  }
  .contact__line {
    display: flex; align-items: center; gap: 8px;
    font-size: 15px; color: var(--accent-green); line-height: 22px;
  }
  .contact__icon { width: 14px; height: 14px; flex: none; }

  .website {
    position: absolute; left: 44px; bottom: 26px;
    font-size: 15px; letter-spacing: 2.6px; color: var(--accent-green);
  }

  .tagline {
    position: absolute; left: 0; right: 0; bottom: 46px;
    text-align: center; font-size: 15px; letter-spacing: 1px;
    color: var(--on-green);
  }
  .tagline__sep { margin: 0 12px; }
</style>
</head>
<body>
<main class="canvas">

  <section class="card card--front" aria-label="Business card front">
    <div class="brand"><span class="brand__mark"></span><span class="brand__name">A Cozy Perch 2 Go</span></div>
    <div class="divider"></div>
    <div class="contact">
      <p class="contact__name">Corabeth Lindqvist</p>
      <p class="contact__line">
        <svg class="contact__icon" viewBox="0 0 16 16" aria-hidden="true">
          <path fill="currentColor" d="M2 5c0-1.5 2.5-2.5 6-2.5s6 1 6 2.5v1.5h-3V5.2c-.9-.3-1.9-.4-3-.4s-2.1.1-3 .4v1.3H2z"/>
          <rect x="3" y="7.5" width="10" height="6.5" rx="1" fill="currentColor"/>
          <circle cx="8" cy="10.7" r="1.8" fill="#fff"/>
        </svg>
        808-555-0173
      </p>
      <p class="contact__line">
        <svg class="contact__icon" viewBox="0 0 16 16" aria-hidden="true">
          <rect x="1" y="3.5" width="14" height="9" fill="currentColor"/>
          <path d="M1.5 4l6.5 5 6.5-5" fill="none" stroke="#fff" stroke-width="1.2"/>
        </svg>
        corabeth@mailbrook.test
      </p>
    </div>
    <p class="website">www.yourwebsite.com</p>
  </section>

  <section class="card card--back" aria-label="Business card back">
    <div class="brand"><span class="brand__mark"></span><span class="brand__name">A Cozy Perch 2 Go</span></div>
    <p class="tagline">Investors<span class="tagline__sep">|</span>Renovators<span class="tagline__sep">|</span>Connectors</p>
  </section>

</main>
</body>
</html>
```